Webseite Toilettenvermietung
Zielgruppe
Wir vermieten mobile Toilettenkabine und Toilettenwagen. Wir haben noch eine Webseite kabinenpark-nord.de und lokus-verleihhaus.de und benötigen noch eine weitere. Es sollen nur die Miettoiletten und Toilettenwagen beworben werden
Aufgabenstellung
saubere und aussageräftige, farbliches Erscheinungsbild der Startseite.

```html
<!DOCTYPE html>
<html lang="de">
<head>
<meta charset="utf-8">
<title>KLARWERK – WC Mietservice</title>
<link href="https://fonts.googleapis.com/css2?family=Roboto:wght@300;400;500;700&display=swap" rel="stylesheet">
<style>
:root{
  --blue:#2a6db5;
  --blue-dark:#1a5aa8;
  --band-top:#2d80cf;
  --band-bottom:#1b5eae;
  --green:#92c010;
  --text:#444;
  --muted:#8a8a8a;
  --light:#f4f4f4;
  --line:#dedede;
  --white:#fff;
}
*{margin:0;padding:0;box-sizing:border-box}
html,body{width:1062px;height:1200px;overflow:hidden;background:var(--white)}
body{font-family:'Roboto',sans-serif;color:var(--text);position:relative}
.abs{position:absolute}
.btn{position:absolute;background:var(--green);color:var(--white);font-weight:400;text-align:center;text-transform:uppercase;font-size:10px;border-radius:1px}

/* header */
.site-header{position:absolute;left:0;top:0;width:1062px;height:39px;background:linear-gradient(#eaf6fa,#fff);border-bottom:1px solid #d8dde0;z-index:2}
.brand{position:absolute;left:200px;top:6px;height:27px;display:flex;align-items:center;gap:6px;font-weight:700;font-size:15px;color:var(--blue-dark);letter-spacing:.5px}
.brand-dot{width:10px;height:10px;border-radius:50%;background:var(--blue-dark)}
.main-nav a{position:absolute;top:14px;font-size:9px;color:#444;text-decoration:none}
.main-nav a.active{color:var(--blue)}

/* hero */
.hero{position:absolute;left:0;top:39px;width:1062px;height:314px;background:radial-gradient(ellipse at 50% 20%,#8fe3e3 0%,#2fa6ad 35%,#0f4e55 65%,#050a0c 100%)}
.hero-title{position:absolute;left:0;width:1062px;top:58px;text-align:center;font-weight:300;font-size:28px;color:#1f6fa8;letter-spacing:.5px}
.hero-text{position:absolute;left:270px;width:522px;top:100px;text-align:center;font-weight:300;font-size:10px;line-height:13.3px;color:#fff}
.hero .btn{left:476px;top:158px;width:110px;height:22px;line-height:22px}
.dots{position:absolute;top:302px;left:484px;display:flex;gap:6px}
.dots span{width:27px;height:2px;background:#fff}
.dots span:first-child{background:var(--blue)}

/* welcome */
.welcome{position:absolute;left:0;top:353px;width:1062px;height:75px;border-bottom:1px solid var(--line)}
.welcome h1{position:absolute;left:0;width:1062px;top:18px;text-align:center;font-weight:400;font-size:17px;line-height:20px;color:var(--blue);text-transform:uppercase}

/* products */
.products{position:absolute;left:0;top:428px;width:1062px;height:326px;background:var(--light)}
.products h2{position:absolute;left:0;width:1062px;top:24px;text-align:center;font-weight:400;font-size:17px;color:#555}
.products .rule{position:absolute;left:499px;top:47px;width:64px;height:2px;background:linear-gradient(90deg,transparent,#bbb,transparent)}
.product{position:absolute;top:62px;width:175px;height:250px}
.product + .product{border-left:1px solid var(--line)}
.product-img{position:absolute;top:0;left:50%;transform:translateX(-50%)}
.product h3{position:absolute;top:114px;width:100%;text-align:center;font-weight:400;font-size:11px;line-height:13.5px;color:var(--blue)}
.product p{position:absolute;top:154px;left:14px;width:147px;text-align:center;font-weight:300;font-size:7px;line-height:9.3px;color:var(--muted);height:45px;overflow:hidden}
.product .btn{top:209px;left:38px;width:100px;height:22px;line-height:22px}

/* services band */
.services{position:absolute;left:0;top:754px;width:1062px;height:184px;background:linear-gradient(var(--band-top),var(--band-bottom));color:#fff}
.services h2{position:absolute;left:199px;top:20px;font-weight:400;font-size:17px;line-height:20px}
.services .intro{position:absolute;left:199px;top:73px;width:170px;font-size:7.5px;line-height:13.3px;font-weight:400}
.service{position:absolute;top:21px;width:120px;text-align:center}
.service .ring{width:53px;height:53px;border:1px solid #fff;border-radius:50%;margin:0 auto;display:flex;align-items:center;justify-content:center}
.service h3{margin-top:14px;font-weight:500;font-size:12px}
.service p{margin-top:5px;font-weight:300;font-size:7.5px;line-height:13.3px;color:#d9e8f7}
.service .more{margin-top:3px;font-weight:500;font-size:8px}

/* about / news */
.about h2,.news h2{position:absolute;top:962px;font-weight:300;font-size:17px;color:#444}
.about h2{left:199px}
.about h2 span{color:var(--blue);font-weight:400}
.about p{position:absolute;left:199px;top:991px;width:370px;font-weight:300;font-size:7.3px;line-height:12.2px;color:var(--muted)}
.divider{position:absolute;left:596px;top:958px;width:1px;height:150px;background:var(--line)}
.news h2{left:624px}
.news .date{position:absolute;left:625px;top:991px;font-size:7.3px;color:#444}
.news .headline{position:absolute;left:625px;top:1003px;font-size:7.3px;color:#444}
.news p{position:absolute;left:625px;top:1015px;width:240px;font-weight:300;font-size:7.3px;line-height:12.2px;color:var(--muted)}
.news .more{position:absolute;left:625px;top:1096px;font-size:7.3px;color:#444}

/* promo */
.promo{position:absolute;left:0;top:1132px;width:1062px;height:46px;background:#f1f1f1;border-top:1px solid var(--line);border-bottom:1px solid var(--line)}
.promo .title{position:absolute;left:356px;top:15px;font-size:13px;color:#555}
.promo .sub{position:absolute;left:538px;top:18px;font-weight:300;font-size:10px;color:#777}
.promo .btn{left:763px;top:13px;width:99px;height:20px;line-height:20px;font-size:10px}
.promo-img{position:absolute;left:212px;top:1092px;width:73px;height:83px;background:linear-gradient(#3aaec8,#1f7f9b);border-radius:4px;z-index:3}

/* footer */
.site-footer{position:absolute;left:199px;top:1183px;display:flex;gap:8px;font-size:7.5px;color:#888}
</style>
</head>
<body>

<header class="site-header">
  <div class="brand"><span class="brand-dot"></span>KLARWERK</div>
  <nav class="main-nav">
    <a class="active" style="left:557px">Startseite</a>
    <a style="left:638px">Miettoiletten</a>
    <a style="left:730px">Toilettenwagen</a>
    <a style="left:832px">Kontakt</a>
  </nav>
</header>

<section class="hero" role="img" aria-label="Konzertpublikum mit erhobenen Händen vor türkis beleuchteter Bühne">
  <div class="hero-title">KOMMSTE MIT?</div>
  <div class="hero-text">Lorem Ipsum is simply dummy text of the printing and typesetting industry.<br>Lorem Ipsum has been the industry's standard dummy text ever since the 1500s, when an unknown printer took a galley of type and scrambled it to make a type specimen book.</div>
  <div class="btn">Contact us</div>
  <div class="dots"><span></span><span></span><span></span></div>
</section>

<section class="welcome">
  <h1>Willkommen bei KLARWERK, Ihr WC Mietservice für mobile WC<br>Kabinen, Wagen &amp; Container</h1>
</section>

<section class="products">
  <h2>Products</h2>
  <div class="rule"></div>

  <article class="product" style="left:181px">
    <div class="product-img" role="img" aria-label="Blaue mobile WC-Kabine" style="top:2px;width:55px;height:96px;background:linear-gradient(90deg,#1f6fc0,#3a95e0);border-radius:8px 8px 2px 2px"></div>
    <h3>Mobile Wc Kabinen<br>Mieten</h3>
    <p>Unsere WC-Kabinen zum mieten bzw im Verleih. Hier finden Sie unsere Toilettenk-abinen wie z. B. das mobile Baustellen WC, unser Universal Miete WC oder den Urinalstand in der Übersicht.</p>
    <div class="btn">Details</div>
  </article>

  <article class="product" style="left:356px">
    <div class="product-img" role="img" aria-label="WC-Container mit mehreren Türen" style="top:18px;width:90px;height:62px;background:linear-gradient(90deg,#9a9aa0,#e6e6ea 40%,#fff);border:3px solid #2c2f7a"></div>
    <h3>Mobile Wc Container<br>Mieten</h3>
    <p>Sie sind auf der Suche nach einem mo-bilen WC Container, bzw. Toilettencontain-er zum mieten? Hier finden Sie unsere mobilen WC Container und WC-Anlagen im Verleih in der Übersicht.</p>
    <div class="btn">Details</div>
  </article>

  <article class="product" style="left:531px">
    <div class="product-img" role="img" aria-label="Graue mobile WC-Kabine" style="top:6px;width:52px;height:84px;background:linear-gradient(90deg,#6f7376,#b0b4b7);border-radius:8px 8px 2px 2px"></div>
    <h3>Mobile Wc Wagen<br>Mieten</h3>
    <p>Hier finden Sie unsere WC Wagen in der Übersicht zur Vermietung, zum Verleih. Vom normalen Toilettenwagen (1x Dame / 1x Herren) bis hin zum exklusiven WC Wagen / Toilettenwagen.</p>
    <div class="btn">Details</div>
  </article>

  <article class="product" style="left:706px">
    <div class="product-img" role="img" aria-label="Weißer Toilettenwagen mit zwei Eingängen" style="top:22px;width:104px;height:52px;background:linear-gradient(#fafafa 70%,#2e3b9a 70%);border:1px solid #ccc"></div>
    <h3>Mobile Wc Anlagen<br>Kaufen</h3>
    <p>Unser Marktplatz. Hier finden Sie div. WC Kabinen, Sanitärcontainer, Toilettenwa-gen, Urinalstände sowie mobile WC Wagen zum verkauf. Neue und geb-rauchte WC Kabinen in verschiedenen</p>
    <div class="btn">Details</div>
  </article>
</section>

<section class="services">
  <h2>KLARWERK<br>Toilettenvermietung</h2>
  <p class="intro">Lorem Ipsum is simply dummy text of the print-ing and typesetting industry.<br>Lorem Ipsum has been the industry's standard dummy text ever since the 1500s when an unknown printer took a galley of type and scrambled it to make a type specimen book.</p>

  <div class="service" style="left:425px">
    <div class="ring">
      <svg width="26" height="26" viewBox="0 0 26 26" fill="none" stroke="#fff" stroke-width="2" stroke-linecap="round"><path d="M20 4 L13 13"/><path d="M8 12 L15 17 L11 22 L5 18 Z" fill="#fff"/><circle cx="20" cy="20" r="1" fill="#fff"/></svg>
    </div>
    <h3>Clean</h3>
    <p>Lorem Ipsum is simply<br>dummy text of the printing and<br>typesetting industry.</p>
    <div class="more">Read More ▸</div>
  </div>

  <div class="service" style="left:587px">
    <div class="ring">
      <svg width="34" height="24" viewBox="0 0 34 24" fill="#fff"><rect x="2" y="3" width="19" height="13"/><path d="M22 7 H28 L32 12 V16 H22 Z"/><circle cx="8" cy="18" r="3.5" stroke="#1f68b8" stroke-width="1.5"/><circle cx="26" cy="18" r="3.5" stroke="#1f68b8" stroke-width="1.5"/></svg>
    </div>
    <h3>Transport</h3>
    <p>Lorem Ipsum is simply<br>dummy text of the printing and<br>typesetting industry.</p>
    <div class="more">Read More ▸</div>
  </div>

  <div class="service" style="left:749px">
    <div class="ring">
      <svg width="28" height="28" viewBox="0 0 28 28" stroke="#fff" stroke-width="4" stroke-linecap="round" fill="none"><path d="M6 6 L22 22"/><path d="M22 6 L6 22"/><circle cx="22" cy="6" r="3" stroke-width="2"/></svg>
    </div>
    <h3>Installation</h3>
    <p>Lorem Ipsum is simply<br>dummy text of the printing and<br>typesetting industry.</p>
    <div class="more">Read More ▸</div>
  </div>
</section>

<section class="about">
  <h2>About <span>KLARWERK</span></h2>
  <p>Lorem Ipsum is simply dummy text of the printing and typesetting industry.<br>Lorem Ipsum has been the industry's standard dummy text ever since the 1500s, when an unknown printer took a galley of type and scrambled it to make a type specimen book.<br>It has survived not only five centuries, but also the leap into electronic typesetting, remaining essentially unchanged.<br>It was popularised in the 1960s with the release of Bogensatz sheets containing Lorem Ipsum passages, and more recently with desktop publishing software like Satzwerk Pro including versions of Lorem Ipsum.<br>Lorem Ipsum is simply dummy text of the printing and typesetting industry.</p>
</section>

<div class="divider"></div>

<section class="news">
  <h2>News &amp; Infos</h2>
  <div class="date">04.02.2014</div>
  <div class="headline">Vermietung von mobilen, behindertengerechter WC Kabinen</div>
  <p>Bei uns erhalten Sie nicht nur herkömmliche Mobil-WCs zur Miete. Ein bundesweiter Service unsers Unternehmens ist die Vermietung behin-dertengerechter WC Kabinen mit den Maßen 1,6 x 1,6 Metern und einer Außenhöhe von 2,30 Metern. Nutzen Sie die komfortable Alter-native der mobilen WC Anlagen für Ihre Veranstaltungen und/oder Baustellen.</p>
  <div class="more">Weitere Meldungen ▸</div>
</section>

<div class="promo-img" role="img" aria-label="Türkisfarbene mobile WC-Kabine"></div>

<section class="promo">
  <div class="title">Mobile Toiletten Zum Kaufen</div>
  <div class="sub">Jetzt In Unserem Marktplaz Stobern</div>
  <div class="btn">Buy it now</div>
</section>

<footer class="site-footer">
  <span>Produkte</span><span>News &amp; Infos</span><span>Unternehmen</span><span>Kontakt</span><span>AGB</span><span>Impressum</span>
</footer>

</body>
</html>
```